i need a business card for a plumbing company in california

we are a drain cleaning , maintenance plumbing company who is starting new marketing campaign for a tatrench-less pipe installation department .

Target Market(s)

the professional who appreciates time and quality workmanship.

Industry/Entity Type

Plumbing

Colors
0655a3
ec1f27

Requirements
Must have
• the second logo needs to be included
Nice to have
• a focus on the services offered
Should not have
• any underlined words on the brief

```html
<!DOCTYPE html>
<html lang="en">
<head>
<meta charset="utf-8">
<title>Flowline Plumbing Co — Business Card</title>
<link href="https://fonts.googleapis.com/css2?family=Open+Sans:ital,wght@0,400;0,600;0,700;1,700&family=Roboto+Condensed:wght@400;700&display=swap" rel="stylesheet">
<style>
  :root {
    --brand-blue: #0655a3;
    --brand-red: #ec1f27;
    --red-dark: #b5141b;
    --red-mid: #d81920;
    --orange: #f15a24;
    --grey-text: #555b61;
    --grey-light: #eceef0;
    --placeholder: #dfe2e6;
    --stage: #e9e9e9;
    --card: #ffffff;
  }
  * { box-sizing: border-box; margin: 0; padding: 0; }
  html, body { width: 726px; height: 1200px; overflow: hidden; }
  body {
    background: var(--stage);
    font-family: "Open Sans", Arial, sans-serif;
    display: flex;
    flex-direction: column;
    align-items: center;
    justify-content: center;
    gap: 70px;
  }
  .card {
    position: relative;
    width: 640px;
    height: 366px;
    background: var(--card);
    overflow: hidden;
    box-shadow: 0 6px 18px rgba(0,0,0,.18);
  }
  .card__shapes { position: absolute; inset: 0; width: 100%; height: 100%; }
  .brand-name {
    position: absolute;
    font-family: "Roboto Condensed", Arial, sans-serif;
    font-weight: 700;
    color: var(--brand-red);
    line-height: 1.02;
    display: flex;
    align-items: center;
    gap: 8px;
  }
  .brand-name__dot {
    width: 14px; height: 14px; border-radius: 50%;
    background: var(--brand-red); flex: none;
  }
  /* Front */
  .front .brand-name { left: 26px; top: 26px; font-size: 26px; }
  .tagline-box {
    position: absolute;
    left: 200px; top: 142px;
    width: 240px; height: 84px;
  }
  .tagline-box svg { position: absolute; inset: 0; width: 100%; height: 100%; }
  .tagline-box__lead {
    position: absolute; left: 78px; top: 10px;
    font-family: "Roboto Condensed", Arial, sans-serif;
    font-size: 18px; color: var(--grey-text);
  }
  .tagline-box__main {
    position: absolute; left: 40px; top: 30px;
    font-style: italic; font-weight: 700;
    font-size: 36px; color: var(--brand-red);
  }
  .services {
    position: absolute; right: 22px; top: 250px;
    width: 250px;
    font-family: "Roboto Condensed", Arial, sans-serif;
    font-size: 12.5px; line-height: 1.35;
    color: var(--grey-text);
  }
  /* Back */
  .owner { position: absolute; left: 28px; top: 24px; }
  .owner__name {
    font-family: "Roboto Condensed", Arial, sans-serif;
    font-size: 32px; font-weight: 700; line-height: 1.1;
    color: var(--brand-red);
  }
  .owner__role { font-size: 14px; font-style: italic; color: var(--grey-text); }
  .contacts {
    position: absolute; left: 30px; top: 150px;
    list-style: none; display: grid; gap: 12px;
  }
  .contacts li {
    display: flex; align-items: center; gap: 10px;
    font-size: 13px; font-weight: 600; color: #333;
  }
  .contacts svg { width: 22px; height: 22px; flex: none; }
  .badge {
    position: absolute; left: 452px; top: 150px;
    width: 92px; height: 92px; border-radius: 50%;
    background: var(--placeholder);
  }
  .back .brand-name { right: 26px; bottom: 30px; font-size: 24px; }
  .socials {
    position: absolute; left: 30px; bottom: 48px;
    display: flex; gap: 6px;
  }
  .socials span {
    width: 22px; height: 22px; border-radius: 50%;
    background: var(--brand-blue);
  }
  .handles {
    position: absolute; left: 0; bottom: 0; width: 420px; height: 34px;
    background: var(--grey-light);
    display: flex; align-items: center; gap: 22px;
    padding-left: 30px;
    font-size: 11px; color: #333;
  }
</style>
</head>
<body>

  <section class="card front" aria-label="Card front">
    <svg class="card__shapes" viewBox="0 0 640 366" preserveAspectRatio="none" aria-hidden="true">
      <polygon points="420,0 640,0 640,60" fill="var(--brand-blue)"/>
      <polygon points="350,0 560,0 640,70 640,120" fill="var(--brand-red)"/>
      <polygon points="470,0 640,0 640,60 560,0" fill="var(--red-dark)"/>
      <polygon points="560,0 640,0 640,30" fill="var(--brand-blue)"/>
      <polygon points="0,250 140,366 0,366" fill="var(--red-dark)"/>
      <polygon points="0,290 220,366 0,366" fill="var(--brand-red)"/>
      <polygon points="0,330 90,366 0,366" fill="var(--orange)"/>
    </svg>
    <div class="brand-name"><span class="brand-name__dot"></span>Flowline<br>Plumbing Co</div>
    <div class="tagline-box">
      <svg viewBox="0 0 240 84" aria-hidden="true">
        <polygon points="10,6 234,2 228,80 4,78" fill="#fff" stroke="#c9cdd1" stroke-width="2"/>
        <polygon points="10,6 60,5 56,12 8,14" fill="var(--brand-red)"/>
      </svg>
      <span class="tagline-box__lead">Lead by</span>
      <span class="tagline-box__main">Example...</span>
    </div>
    <p class="services">Virgin Trench-Less Installs &amp; Replacements-<br>Pipe Bursting &amp; Pipe Piercing Install,<br>Replace, Pipe Enlargement. PULL &amp; GO</p>
  </section>

  <section class="card back" aria-label="Card back">
    <svg class="card__shapes" viewBox="0 0 640 366" preserveAspectRatio="none" aria-hidden="true">
      <polygon points="300,0 640,0 640,110 430,80" fill="var(--brand-red)"/>
      <polygon points="440,0 640,0 640,90 520,60" fill="var(--red-mid)"/>
      <polygon points="560,0 640,0 640,50" fill="var(--red-dark)"/>
      <polygon points="430,80 640,110 640,124 470,96" fill="var(--brand-blue)"/>
      <polygon points="420,366 640,260 640,366" fill="var(--grey-light)"/>
    </svg>
    <div class="owner">
      <p class="owner__name">Marco Delgado Jr</p>
      <p class="owner__role">Owner</p>
    </div>
    <ul class="contacts">
      <li>
        <svg viewBox="0 0 22 22" aria-hidden="true"><rect width="22" height="22" rx="3" fill="var(--brand-blue)"/><path d="M7 5l3 3-1.5 1.5a8 8 0 0 0 4 4L14 12l3 3-2 2C10 17 5 12 5 7z" fill="#fff"/></svg>
        2095550148
      </li>
      <li>
        <svg viewBox="0 0 22 22" aria-hidden="true"><rect width="22" height="22" rx="3" fill="var(--brand-blue)"/><rect x="5" y="7" width="12" height="8" fill="none" stroke="#fff" stroke-width="1.5"/><path d="M5 7l6 5 6-5" fill="none" stroke="#fff" stroke-width="1.5"/></svg>
        info@flowlineplumbingco.com
      </li>
      <li>
        <svg viewBox="0 0 22 22" aria-hidden="true"><rect width="22" height="22" rx="3" fill="var(--brand-blue)"/><circle cx="11" cy="11" r="6" fill="none" stroke="#fff" stroke-width="1.5"/><path d="M5 11h12M11 5c-3 3-3 9 0 12M11 5c3 3 3 9 0 12" fill="none" stroke="#fff" stroke-width="1.2"/></svg>
        www.flowlineplumbingco.com
      </li>
    </ul>
    <div class="badge" role="img" aria-label="Department logo placeholder"></div>
    <div class="socials" aria-hidden="true"><span></span><span></span><span></span><span></span><span></span></div>
    <div class="handles">
      <span>/Facebook@FlowlinePlumbing</span>
      <span>FlowlinePlumbing</span>
    </div>
    <div class="brand-name"><span class="brand-name__dot"></span>Flowline<br>Plumbing Co</div>
  </section>

</body>
</html>
```